Buchcover-Design für Buch der Schleier-Biografie gesucht
Zielgruppe
Das Genre nennt sich Schleier-Biografie. Typischerweise sind es Leserinnen, die sich vom fremden Schicksal berühren lassen wollen. Die Bücher stellen Unterdrückung und Gewalt gegen Frauen dar, aber immer auch eine Befreiung.
Einige typische Cover habe ich beigefügt. Wichtig ist, dass die Autorin anonym bleiben will.
Aufgabenstellung
Autoren:
Jonas Kolbwetter
Dilan K.
Ich benötige ein deutsches und ein englisches Cover:
Titel: Die stille Mauer
Untertitel: Wie ich mein Zuhause verließ und neu anfing
Titel: The Quiet Wall
Untertitel: How I left my home and found a new start
Dies wird der Text bei Buchplatz sein:
“Talaq”, sagte er, als lese er aus seinem arabischen Buch vor. “Frau, ich verstoße dich.”
Meine Mutter sah auf. Ihre großen Augen lagen in seinem Blick. Meine schöne Mutter, ihr Gesicht ganz bleich.
“Talaq”, sagte er wieder. “Ich verstoße dich, Sirwe.”
“Nein”, flüsterte sie. “Das kannst du nicht tun. Die Kinder - “
“Talaq, du bist verstoßen. Verlasse mein Haus, verlasse deine Kinder.”
Ich bin Dilan. - Am Anfang des Buches komme ich in den Kindergarten, eine kleine Kurdin aus Erbil im Nordirak. Mein Vater ist alt und strenggläubig, meine Mutter ist jung und hübsch. Als er die Scheidung gegen sie ausspricht - das dreimalige Talaq - muss sie ohne ihre Kinder das Haus verlassen. So ist es üblich im Islam, denn die Kinder gehören dem Mann.
Wo mein Leben in meiner Erinnerung anfängt, beginnt es wie ein deutsches Märchen. So viel habe ich in dem Märchen Aschenputtel von mir gefunden, dass ich denke, mein kurdisches Leben ist nichts anders als ein deutsches Märchen, das man den Kindern erzählt, damit sie sich fürchten.
Also handelt dieses Buch von einem Mädchen, das in die Finsternis und in den Schmutz gestoßen wird. Und doch bin ich ein Mädchen von Millionen, denn dort wo ich herkomme, ist jedes Mädchen ein Aschenputtel. Das glückliche Ende des Märchens - davon träumen sie vergeblich. Und ihr Märchenprinz - das ist ein Mann, der sie nicht schlägt.
Ich werde erzählen, wie ich versucht habe, meinen Vater und seinen Gott zu verstehen. Es macht mir ein wenig Angst, darüber zu schreiben – das sollten Sie wissen. In diesem Buch ist deshalb alles ..

```html
<!DOCTYPE html>
<html lang="de">
<head>
<meta charset="utf-8">
<title>Die stille Mauer – Umschlag</title>
<link rel="stylesheet" href="https://fonts.googleapis.com/css2?family=Cinzel:wght@400;500&family=Open+Sans:wght@300;400&display=swap">
<style>
  :root {
    --stage: #2f2f30;
    --navy: #1d3a63;
    --navy-deep: #183257;
    --ornament: #3f6396;
    --frame-line: #7f9cc7;
    --ink-light: #ffffff;
    --ink-soft: #d7e1ef;
    --photo-dark: #120c09;
    --photo-mid: #3b2417;
    --photo-warm: #7a4a2c;
  }
  * { box-sizing: border-box; margin: 0; padding: 0; }
  html, body { width: 892px; height: 1200px; overflow: hidden; background: var(--stage); }
  .canvas { position: relative; width: 892px; height: 1200px; }
  .spread {
    position: absolute; left: 20px; top: 315px;
    width: 852px; height: 569px; display: flex;
    box-shadow: 0 4px 18px rgba(0,0,0,.45);
  }

  /* Back cover */
  .back-cover { position: relative; width: 394px; height: 100%; background: var(--navy); }
  .ornament-border {
    position: absolute; inset: 14px 18px 14px 18px;
    background: linear-gradient(135deg, var(--ornament), #345784 50%, var(--ornament));
    opacity: .55;
  }
  .blurb-panel {
    position: absolute; left: 56px; top: 58px; width: 281px; height: 482px;
    background: var(--navy-deep);
    border: 1px solid var(--frame-line);
    outline: 1px solid var(--frame-line); outline-offset: -4px;
    padding: 26px 22px 18px;
    display: flex; flex-direction: column; align-items: center;
    color: var(--ink-light);
  }
  .blurb-panel .title-block { font-size: .62em; }
  .blurb-text {
    margin-top: 20px; width: 100%;
    font-family: "Open Sans", sans-serif; font-size: 6.2px; line-height: 1.35;
  }
  .blurb-text p + p { margin-top: 6px; }
  .back-author {
    margin-top: auto;
    font-family: "Open Sans", sans-serif; font-weight: 300; font-size: 10.5px;
    color: var(--ink-soft); letter-spacing: .3px;
  }

  /* Title block shared */
  .title-block { text-align: center; font-family: "Cinzel", serif; color: var(--ink-light); line-height: 1; }
  .title-rule { display: flex; align-items: center; justify-content: center; gap: 6px; }
  .title-rule .rule { height: 1px; width: 7em; background: var(--ink-soft); }
  .title-rule .dot { width: .28em; height: .28em; border: 1px solid var(--ink-soft); transform: rotate(45deg); }
  .title-small { font-size: 2.4em; }
  .title-large { font-size: 3.3em; letter-spacing: -.5px; }
  .subtitle { font-size: 1.05em; letter-spacing: 1.5px; margin-top: .35em; line-height: 1.45; }

  /* Spine */
  .spine { position: relative; width: 64px; height: 100%; background: var(--navy); overflow: hidden; }
  .spine-content {
    position: absolute; left: 32px; top: 284.5px;
    width: 569px; height: 64px;
    transform: translate(-50%, -50%) rotate(-90deg);
    display: flex; align-items: center; padding: 0 24px 0 18px; gap: 14px;
    color: var(--ink-light);
  }
  .spine-author { font-family: "Open Sans", sans-serif; font-weight: 300; font-size: 11px; line-height: 1.1; color: var(--ink-soft); }
  .spine-title { font-family: "Cinzel", serif; font-size: 29px; white-space: nowrap; margin-left: 14px; }
  .spine-divider { width: 1px; height: 16px; background: var(--ink-soft); }
  .spine-subtitle { font-family: "Cinzel", serif; font-size: 8.5px; line-height: 1.25; letter-spacing: .8px; text-transform: uppercase; }

  /* Front cover */
  .front-cover { position: relative; width: 394px; height: 100%; background: var(--photo-dark); overflow: hidden; }
  .cover-photo {
    position: absolute; inset: 0;
    background:
      radial-gradient(ellipse 55% 45% at 62% 58%, var(--photo-warm) 0%, var(--photo-mid) 45%, transparent 75%),
      radial-gradient(ellipse 70% 60% at 60% 40%, #2a1a11 0%, transparent 70%),
      var(--photo-dark);
  }
  .cover-shade { position: absolute; left: 0; right: 0; bottom: 0; height: 45%; background: linear-gradient(transparent, rgba(10,7,6,.92) 55%); }
  .front-author {
    position: absolute; top: 36px; width: 100%; text-align: center;
    font-family: "Open Sans", sans-serif; font-weight: 300; font-size: 21px;
    color: var(--ink-light); letter-spacing: .6px;
  }
  .front-cover .title-block { position: absolute; left: 0; right: 0; top: 356px; font-size: 15px; }
  .front-cover .title-rule .rule { width: 8.5em; }
</style>
</head>
<body>
<main class="canvas">
  <section class="spread" aria-label="Buchumschlag Die stille Mauer">

    <article class="back-cover">
      <div class="ornament-border" role="img" aria-label="Florales Rankenornament in hellem Blau als Rahmen"></div>
      <div class="blurb-panel">
        <div class="title-block">
          <div class="title-rule"><span class="rule"></span><span class="dot"></span><span class="title-small">Die</span><span class="dot"></span><span class="rule"></span></div>
          <div class="title-large">Stille</div>
          <div class="title-large">Mauer</div>
          <div class="subtitle">Wie ich mein Zuhause verließ<br>und neu anfing</div>
        </div>
        <div class="blurb-text">
          <p>“Talaq”, sagte er, als lese er aus seinem arabischen Buch vor. “Frau, ich verstoße dich.”<br>
          Meine Mutter sah auf. Ihre großen Augen lagen in seinem Blick. Meine schöne Mutter, ihr Gesicht ganz bleich.<br>
          “Talaq”, sagte er wieder. “Ich verstoße dich, Sirwe.”<br>
          “Nein”, flüsterte sie. “Das kannst du nicht tun. Die Kinder - ”<br>
          “Talaq, du bist verstoßen. Verlasse mein Haus, verlasse deine Kinder.”</p>
          <p>Ich bin Dilan. - Am Anfang des Buches komme ich in den Kindergarten, eine kleine Kurdin aus Erbil im Nordirak. Mein Vater ist alt und strenggläubig, meine Mutter ist jung und hübsch. Als er die Scheidung gegen sie ausspricht - das dreimalige Talaq - muss sie ohne ihre Kinder das Haus verlassen. So ist es üblich im Islam, denn die Kinder gehören dem Mann.</p>
          <p>Wo mein Leben in meiner Erinnerung anfängt, beginnt es wie ein deutsches Märchen. So viel habe ich in dem Märchen Aschenputtel von mir gefunden, dass ich denke, mein kurdisches Leben ist nichts anders als ein deutsches Märchen, das man den Kindern erzählt, damit sie sich fürchten.</p>
          <p>Also handelt dieses Buch von einem Mädchen, das in die Finsternis und in den Schmutz gestoßen wird. Und doch bin ich ein Mädchen von Millionen, denn dort wo ich herkomme, ist jedes Mädchen ein Aschenputtel. Das glückliche Ende des Märchens - davon träumen sie vergeblich. Und ihr Märchenprinz - das ist ein Mann, der sie nicht schlägt.</p>
          <p>Ich werde erzählen, wie ich versucht habe, meinen Vater und seinen Gott zu verstehen. Es macht mir ein wenig Angst, darüber zu schreiben – das sollten Sie wissen. In diesem Buch ist deshalb alles von mir, nur mein Name fehlt.</p>
        </div>
        <div class="back-author">Jonas Kolbwetter &amp; Dilan K.</div>
      </div>
    </article>

    <aside class="spine">
      <div class="spine-content">
        <div class="spine-author">Jonas Kolbwetter<br>&amp; Dilan K.</div>
        <div class="spine-title">The Quiet Wall</div>
        <div class="spine-divider"></div>
        <div class="spine-subtitle">How I left my home<br>and found a new start</div>
      </div>
    </aside>

    <article class="front-cover">
      <div class="cover-photo" role="img" aria-label="Fotografie einer Frau mit braunem Schleier, nur ein blaues Auge sichtbar, vor dunklem Hintergrund"></div>
      <div class="cover-shade"></div>
      <div class="front-author">Jonas Kolbwetter &amp; Dilan K.</div>
      <div class="title-block">
        <div class="title-rule"><span class="rule"></span><span class="dot"></span><span class="title-small">Die</span><span class="dot"></span><span class="rule"></span></div>
        <div class="title-large">Stille</div>
        <div class="title-large">Mauer</div>
        <div class="subtitle">Wie ich mein Zuhause verließ<br>und neu anfing</div>
      </div>
    </article>

  </section>
</main>
</body>
</html>
```